キャリア層をターゲットとしたセミナーを開催予定です。落ち着いた雰囲気のデザインをお願いします。(講演内容は添付ファイルをご確認ください)
開催団体:一般社団法人あおぞら地域交流センター
〒521-0342滋賀県米原市柏原台4-7-15
TEL:0749-38-2951
TEL:0120-394-667
A4
片面
• 高解像度JPG (.jpg)

洗練されたデザインや文字の配置、対象となるターゲットにフィットすると思い選択いたしました。
ご提案ありがとうございました。

皆さま、貴重なアイディアをくださり本当にありがとうございました。
どれか一つ選択することが大変心苦しいのですが、
今回このような結果を出させていただきました。
今後ともよろしくお願いいたします。

```html
<!DOCTYPE html>
<html lang="ja">
<head>
<meta charset="utf-8">
<title>言葉が人を動かす、自分を変える｜オンライン講座</title>
<link href="https://fonts.googleapis.com/css2?family=Noto+Sans+JP:wght@400;500;700;900&family=Jost:wght@300;400;500&display=swap" rel="stylesheet">
<style>
:root{
  --green:#76ad95;
  --green-dark:#5d957d;
  --ink:#363a3a;
  --sub:#5a5f5e;
  --paper:#f2f3f1;
  --card:#ffffff;
  --line:#c9cecb;
}
*{margin:0;padding:0;box-sizing:border-box}
html,body{width:846px;height:1200px;overflow:hidden}
body{background:var(--paper);font-family:"Noto Sans JP",sans-serif;color:var(--ink);position:relative}
.visual{position:absolute;left:420px;top:0;width:426px;height:470px;
  background:radial-gradient(ellipse at 55% 40%,#ffffff 0%,#e4e7e5 45%,#cfd4d1 100%)}
.hand{position:absolute;left:430px;top:400px;width:390px;height:60px;border-radius:40px 40px 8px 8px;
  background:linear-gradient(180deg,#d9c4b4,#c6ab98);opacity:.55}
.tag{position:absolute;left:50px;top:50px;display:flex;gap:12px;align-items:center}
.tag-course{border-left:6px solid var(--green);padding-left:10px;line-height:1.25}
.tag-course b{display:block;font-size:20px;color:var(--green-dark);font-weight:700}
.tag-course span{font-size:13px;color:var(--sub)}
.tag-free{background:var(--green);color:#fff;font-size:26px;font-weight:700;padding:6px 14px;letter-spacing:2px}
.headline{position:absolute;left:48px;top:112px;font-weight:900;line-height:1.1;letter-spacing:2px}
.headline .l1{font-size:80px;display:block}
.headline .l1 small{font-size:52px}
.headline .l2,.headline .l3{font-size:58px;display:block}
.lead{position:absolute;left:50px;top:338px;font-size:18px;font-weight:500;color:var(--sub);white-space:nowrap}
.date{position:absolute;left:48px;top:372px;display:flex;align-items:flex-end;gap:18px}
.date .day{font-family:"Jost",sans-serif;font-size:78px;font-weight:400;line-height:1;color:var(--ink)}
.date .wd{font-size:26px;font-weight:700}
.date .time{font-family:"Jost",sans-serif;font-size:28px;line-height:1.2;white-space:nowrap}
.date .time small{display:block;font-family:"Noto Sans JP",sans-serif;font-size:13px;color:var(--sub)}
.rule{position:absolute;left:50px;right:26px;top:475px;border-top:1px solid var(--line)}
.col-left{position:absolute;left:50px;top:495px;width:345px}
.col-left h2{font-size:20px;font-weight:700;margin-bottom:10px;line-height:1.4}
.col-left p{font-size:13.5px;line-height:1.75;color:var(--sub);margin-bottom:10px}
.col-left h2.second{margin-top:18px}
.col-right{position:absolute;left:425px;top:495px;width:395px}
.meta{display:flex;gap:12px;align-items:center;font-size:16px;font-weight:700}
.meta span.k{background:var(--card);border:1px solid var(--line);font-size:12px;padding:3px 8px;font-weight:500}
.meta span.v{margin-right:14px}
.box{margin-top:16px;background:var(--card);border:1px solid var(--line);padding:16px 18px}
.box .q{font-size:12px;color:var(--green-dark);font-weight:700}
.box h3{font-size:20px;font-weight:700;border-bottom:2px solid var(--green);padding-bottom:6px;margin-bottom:10px}
.box ul{list-style:none}
.box li{font-size:14px;line-height:1.9;padding-left:16px;position:relative}
.box li::before{content:"";position:absolute;left:0;top:11px;width:8px;height:8px;background:var(--green)}
.speaker{margin-top:14px;font-size:18px;font-weight:700}
.home{margin-top:14px;background:var(--green);color:#fff;display:flex;align-items:center;gap:16px;padding:14px 18px}
.home svg{flex:none}
.home b{font-size:22px;display:block}
.home span{font-size:12px;line-height:1.5}
.footer{position:absolute;left:26px;right:26px;top:965px;height:185px;background:var(--card);display:flex;align-items:center;padding:0 24px;gap:22px}
.org{display:flex;align-items:center;gap:10px;white-space:nowrap}
.org .mark{width:42px;height:42px;border-radius:50%;background:var(--green)}
.org .name{font-size:26px;font-weight:700;color:var(--green-dark)}
.org-info{font-size:12px;line-height:1.7;color:var(--sub);white-space:nowrap}
.org-info b{font-size:12.5px;color:var(--ink)}
.contact{margin-left:auto;text-align:left;white-space:nowrap}
.contact .lbl{font-size:13px;font-weight:700;color:var(--green-dark)}
.contact .tel{display:flex;align-items:center;gap:6px;font-family:"Jost",sans-serif;font-size:34px;font-weight:500;line-height:1.15}
.contact small{display:block;font-size:11px;color:var(--sub)}
.contact .web{display:inline-block;margin-top:4px;font-size:13px;border:1px solid var(--line);padding:2px 10px}
</style>
</head>
<body>
<div class="visual" role="img" aria-label="Yes, we can! と書かれた吹き出しの立体オブジェの写真"></div>
<div class="hand" role="img" aria-label="吹き出しを差し出す手のひらの写真"></div>

<div class="tag">
  <div class="tag-course"><b>オンライン講座</b><span>地域の学び応援プログラム</span></div>
  <div class="tag-free">受講無料</div>
</div>

<h1 class="headline"><span class="l1">言葉<small>が</small></span><span class="l2">人を動かす、</span><span class="l3">自分を変える</span></h1>

<p class="lead">ハミルトン元大統領のスピーチに隠された伝える力とは？</p>

<div class="date">
  <div class="day">9.24<span class="wd">(金)</span></div>
  <div class="time">19:00〜20:00<small>受付開始 18:45〜</small></div>
</div>

<div class="rule"></div>

<section class="col-left">
  <h2>日本人はユーモアが言えない…</h2>
  <p>会議や商談、プレゼンテーションで緊張してしまい、伝えたいことが半分も伝わらなかった経験はありませんか。言葉の選び方と間の取り方を学ぶことで、相手の心に届く話し方は誰でも身につけられます。</p>
  <h2 class="second">授業中の発表で突然襲ってきた声の震え…</h2>
  <p>学生時代の小さな失敗が、大人になっても人前で話す苦手意識として残っている方は少なくありません。本講座では原因をひもとき、自信を持って話すための具体的な方法をお伝えします。</p>
  <p>明日から使える実践的なワークも交えて、楽しく学びましょう。</p>
</section>

<section class="col-right">
  <div class="meta"><span class="k">オンライン</span><span class="v">60分講座</span><span class="k">定員</span><span class="v">10名</span></div>
  <div class="box">
    <p class="q">こんな方におすすめ</p>
    <h3>どうして人前であがってしまうのか</h3>
    <ul>
      <li>講師の自己紹介が苦手だった3つのこと</li>
      <li>あがり症が治らない原因とその対処法</li>
      <li>緊張が一瞬でほぐれる簡単ワーク</li>
      <li>あがり症改善のための実践トレーニング</li>
      <li>話し方ひとつで印象を大きく変えるコツ</li>
    </ul>
  </div>
  <p class="speaker">【講師】あがり症改善講師</p>
  <div class="home">
    <svg width="58" height="40" viewBox="0 0 58 40" aria-hidden="true"><rect x="9" y="3" width="40" height="26" rx="2" fill="none" stroke="#fff" stroke-width="3"/><path d="M2 34h54l-4 4H6z" fill="#fff"/></svg>
    <div><b>自宅で学べる</b><span>お申し込み後に参加用URLをお送りします。<br>パソコン・スマートフォンから受講できます。</span></div>
  </div>
</section>

<footer class="footer">
  <div class="org"><span class="mark"></span><span class="name">あおぞら</span></div>
  <div class="org-info">
    <b>主催：一般社団法人あおぞら地域交流センター</b><br>
    〒521-0342滋賀県米原市柏原台4-7-15<br>
    TEL：0749-38-2951
  </div>
  <div class="contact">
    <div class="lbl">受講お申し込み</div>
    <div class="tel"><svg width="26" height="26" viewBox="0 0 24 24" aria-hidden="true"><path fill="#5d957d" d="M6.6 10.8a15 15 0 0 0 6.6 6.6l2.2-2.2a1 1 0 0 1 1-.25 11 11 0 0 0 3.6.6 1 1 0 0 1 1 1V20a1 1 0 0 1-1 1A17 17 0 0 1 3 4a1 1 0 0 1 1-1h3.5a1 1 0 0 1 1 1 11 11 0 0 0 .6 3.6 1 1 0 0 1-.25 1z"/></svg>0120-394-667</div>
    <small>受付時間 平日9時〜17時</small>
    <span class="web">aozora-koryu.or.jp</span>
  </div>
</footer>
</body>
</html>
```